business card design for heron textile printing

Heron Textile Printing requires elegant and colorful designs for its business card, ensuring both are visually cohesive and reflect the brand’s creative, modern identity. The logo is already finalized and should be a central element in designs.

## Business Card Design Brief

- Feature the logo clearly, with colors and style matching the letterhead.
- Present contact information (name, title, phone, email, website, address) in a clear, organized manner.
- Open to creative layouts, finishes, and double-sided designs, as long as the card remains professional and easy to read.
- Ensure both pieces feel unified as part of the same brand identity.

The final designs should be vibrant, professional, and memorable, showcasing Heron Textile Printing’s creative spirit.

Target Market(s)

Pakistan

Industry/Entity Type

Textile printing

Other font styles liked:
• Calibri

Requirements
Must have
• Address Email Address Phone number designer can ask me when start designing

```html
<!DOCTYPE html>
<html lang="en">
<head>
<meta charset="utf-8">
<title>Heron Textile Printing – Business Card</title>
<link rel="stylesheet" href="https://fonts.googleapis.com/css2?family=Montserrat:wght@400;500;600;700&display=swap">
<style>
  :root {
    --backdrop: #2f2f30;
    --card: #f4ebe0;
    --maroon: #5a1d22;
    --purple: #a1168c;
    --orange: #f0531c;
    --ink: #2a2222;
    --rule: #2b2323;
  }
  * { box-sizing: border-box; margin: 0; padding: 0; }
  html, body {
    width: 1200px; height: 694px; overflow: hidden;
    background: var(--backdrop);
    font-family: "Montserrat", sans-serif;
  }
  .sheet {
    position: relative; width: 1200px; height: 694px;
    display: flex; align-items: center; justify-content: center; gap: 40px;
  }
  .card {
    position: relative;
    width: 540px; height: 309px;
    background: var(--card);
    border-radius: 24px;
    box-shadow: 0 18px 40px rgba(0,0,0,.45);
    overflow: hidden;
  }

  /* Front */
  .card--front { display: flex; align-items: center; justify-content: center; }
  .brand { display: flex; align-items: center; gap: 14px; }
  .brand__dot {
    width: 46px; height: 46px; border-radius: 50%;
    background: var(--orange); flex: none;
  }
  .brand__name {
    color: var(--maroon); font-weight: 600;
    font-size: 27px; line-height: 1.1; letter-spacing: .5px;
  }
  .brand--small { gap: 8px; }
  .brand--small .brand__dot { width: 22px; height: 22px; }
  .brand--small .brand__name { font-size: 13px; letter-spacing: .3px; }

  /* Back */
  .card--back .brand { position: absolute; top: 44px; right: 34px; }
  .holder { position: absolute; left: 34px; top: 118px; }
  .holder__name { color: var(--purple); font-weight: 700; font-size: 27px; line-height: 1.1; }
  .holder__title { color: var(--ink); font-weight: 500; font-size: 13px; margin-top: 6px; }
  .divider {
    position: absolute; left: 34px; right: 34px; top: 184px;
    height: 1px; background: var(--rule);
  }
  .contacts {
    position: absolute; left: 34px; top: 200px;
    list-style: none; display: grid; gap: 9px;
  }
  .contacts li {
    display: flex; align-items: center; gap: 10px;
    color: var(--ink); font-size: 13px; font-weight: 400;
  }
  .contacts svg { width: 16px; height: 16px; flex: none; }
  .address {
    position: absolute; right: 34px; top: 204px;
    text-align: right; color: var(--ink);
    font-size: 13px; line-height: 1.55; font-style: normal;
  }
</style>
</head>
<body>
<main class="sheet">
  <section class="card card--front" aria-label="Business card front">
    <div class="brand">
      <span class="brand__dot"></span>
      <span class="brand__name">Heron Textile Printing</span>
    </div>
  </section>

  <section class="card card--back" aria-label="Business card back">
    <div class="brand brand--small">
      <span class="brand__dot"></span>
      <span class="brand__name">Heron Textile Printing</span>
    </div>

    <div class="holder">
      <p class="holder__name">Daniel Reed</p>
      <p class="holder__title">Owner</p>
    </div>

    <div class="divider"></div>

    <ul class="contacts">
      <li>
        <svg viewBox="0 0 16 16" aria-hidden="true"><circle cx="8" cy="8" r="8" fill="var(--orange)"/><path d="M5.2 4.2l1.6-.4.8 2-1 .8a5 5 0 0 0 2.8 2.8l.8-1 2 .8-.4 1.6c-3.6.2-6.8-3-6.6-6.6z" fill="#fff"/></svg>
        041-555 302 118
      </li>
      <li>
        <svg viewBox="0 0 16 16" aria-hidden="true"><rect x="1" y="3" width="14" height="10" rx="1" fill="var(--orange)"/><path d="M1.5 3.8L8 9l6.5-5.2" fill="none" stroke="#fff" stroke-width="1.2"/></svg>
        info@heronprint.pk
      </li>
      <li>
        <svg viewBox="0 0 16 16" aria-hidden="true"><circle cx="8" cy="8" r="8" fill="var(--orange)"/><circle cx="8" cy="8" r="5" fill="none" stroke="#fff" stroke-width="1"/><path d="M3 8h10M8 3c-2.2 2.8-2.2 7.2 0 10M8 3c2.2 2.8 2.2 7.2 0 10" fill="none" stroke="#fff" stroke-width="1"/></svg>
        www.heronprinting.pk
      </li>
    </ul>

    <address class="address">
      17, Mill Road, Civil Lines<br>
      38000, Faisalabad, Pakistan
    </address>
  </section>
</main>
</body>
</html>
```